Postcard Design hearing aid sales & service. Free hearing test . Fresh batteries

Bluebonnet Hearing Aid Device Center . Located at 417 Marwick Ln Abilene Texas 79488 Ph 325-555-0147.
Hours Mon thru Thurs 9:00am - 5:00pm closed for lunch 12:00pm - 1:00pm . Fri open 9:00am - 1:00pm
Hearing Test n/c Hearing aid adjustment & cleaning of hearing aids n/c . Fresh batteries buy one 1/2 off on 2nd pack. Limited time. Walk-in welcome Appointments appreciated. THIS MONTH ONLY Special discounts on new state of the art hearing aids w/remote. .

```html
<!DOCTYPE html>
<html lang="en">
<head>
<meta charset="utf-8">
<title>Bluebonnet Hearing Aid Device Center – Postcard</title>
<link rel="stylesheet" href="https://fonts.googleapis.com/css2?family=Fjalla+One&family=Tinos:ital,wght@0,700;1,700&family=Questrial&display=swap">
<style>
  :root {
    --page: #ffffff;
    --navy-top: #122a45;
    --blue-bottom: #0a74c4;
    --navy-top-2: #15212f;
    --blue-bottom-2: #0a70c0;
    --banner: #2b1a7a;
    --banner-edge: #9aa6c8;
    --white: #ffffff;
    --panel-blue: #0c82d2;
    --pill-blue: #1c9be2;
    --pill-grey: #cfcfcf;
    --ink-dark: #1b1b1b;
    --yellow: #ffee1a;
    --gold: #f2b51c;
    --badge-grey: #6f7175;
  }
  * { box-sizing: border-box; margin: 0; padding: 0; }
  html, body { width: 887px; height: 1200px; overflow: hidden; background: var(--page); }
  .sheet { position: relative; width: 887px; height: 1200px; }

  .card { position: absolute; width: 818px; overflow: hidden; color: var(--white); }
  .card--front { left: 30px; top: 40px; height: 543px;
    background: linear-gradient(180deg, var(--navy-top) 0%, #0d4f8a 45%, var(--blue-bottom) 100%); }
  .card--back { left: 35px; top: 621px; height: 541px;
    background: linear-gradient(180deg, var(--navy-top-2) 0%, #0f3f6c 50%, var(--blue-bottom-2) 100%); }

  .banner { position: absolute; }
  .banner svg { position: absolute; inset: 0; }
  .banner__title { position: relative; font-family: "Fjalla One", sans-serif; color: var(--white);
    white-space: nowrap; letter-spacing: 0.3px; }
  .card--front .banner { left: 22px; top: 0; width: 775px; height: 112px; }
  .card--front .banner__title { font-size: 46px; text-align: center; line-height: 104px; }
  .card--back .banner { left: 0; top: 24px; width: 624px; height: 56px; }
  .card--back .banner__title { font-size: 35px; line-height: 56px; padding-left: 26px; }

  .services { position: absolute; left: 0; right: 0; top: 128px; text-align: center;
    font-family: "Tinos", serif; font-style: italic; font-weight: 700; font-size: 21px; line-height: 27px; }

  .offer-box { position: absolute; left: 92px; top: 241px; width: 634px; height: 111px;
    background: var(--panel-blue); border: 3px solid var(--white); border-radius: 24px;
    font-family: "Tinos", serif; font-weight: 700; font-size: 24px; line-height: 32px;
    text-align: center; padding-top: 7px; }

  .located { position: absolute; left: 0; height: 25px; padding: 0 22px 0 40px;
    border-radius: 0 13px 13px 0; font-family: "Questrial", sans-serif; font-size: 17px; line-height: 25px; }
  .card--front .located { top: 378px; background: var(--pill-blue); color: var(--white); }
  .card--back .located { top: 384px; background: var(--pill-grey); color: var(--ink-dark); }

  .contact { position: absolute; left: 40px; font-family: "Questrial", sans-serif; }
  .contact__line { white-space: nowrap; }
  .card--front .contact { top: 414px; }
  .card--front .contact__line--big { font-size: 21px; line-height: 26px; }
  .card--front .contact__line--small { font-size: 17px; line-height: 23px; }
  .card--back .contact { top: 420px; }
  .card--back .contact__line--big { font-size: 18px; line-height: 23px; }
  .card--back .contact__line--small { font-size: 18px; line-height: 24px; }
  .card--back .contact__line--gap { margin-top: 8px; }

  .badge { position: absolute; left: 652px; top: 364px; width: 152px; height: 152px; }
  .badge__text { font-family: "Fjalla One", sans-serif; font-size: 27px; fill: var(--white); }

  .promo { position: absolute; left: 28px; top: 96px; font-family: "Tinos", serif; font-weight: 700; }
  .promo__welcome { color: var(--yellow); font-size: 37px; line-height: 42px; }
  .promo__sub { font-size: 23px; line-height: 30px; }
  .promo__headline { font-size: 41px; line-height: 48px; margin-top: 2px; }
  .promo__detail { font-size: 23px; line-height: 38px; }
</style>
</head>
<body>
<main class="sheet">

  <section class="card card--front">
    <header class="banner">
      <svg width="775" height="112" viewBox="0 0 775 112" aria-hidden="true">
        <polygon points="14,0 761,0 775,112 0,112" fill="var(--banner)"/>
        <polyline points="761,0 775,112 0,112" fill="none" stroke="var(--banner-edge)" stroke-width="2"/>
      </svg>
      <h1 class="banner__title">Bluebonnet Hearing Aid Device Center.</h1>
    </header>

    <p class="services">
      Hearing Test n/c Hearing aid adjustment &amp; cleaning of hearing aids n/c .<br>
      Fresh batteries buy one 1/2 off on 2nd pack.
    </p>

    <div class="offer-box">
      Walk-in welcome Appointments appreciated.<br>
      THIS MONTH ONLY Special discounts on<br>
      new state of the art hearing aids w/remote.
    </div>

    <div class="located">Located at</div>
    <address class="contact" style="font-style:normal">
      <div class="contact__line contact__line--big">417 Marwick Ln Abilene Texas 79488</div>
      <div class="contact__line contact__line--big">Ph 325-555-0147.</div>
      <div class="contact__line contact__line--small">Hours Mon thru Thurs 9:00am - 5:00pm</div>
      <div class="contact__line contact__line--small">Closed for lunch 12:00pm - 1:00pm . Open 9:00am - 1:00pm</div>
    </address>

    <svg class="badge" viewBox="-76 -76 152 152" aria-label="Limited time">
      <polygon fill="var(--gold)" points="0,-76 8,-62 19,-73 24,-58 38,-66 38,-50 54,-54 50,-38 66,-38 58,-24 73,-19 62,-8 76,0 62,8 73,19 58,24 66,38 50,38 54,54 38,50 38,66 24,58 19,73 8,62 0,76 -8,62 -19,73 -24,58 -38,66 -38,50 -54,54 -50,38 -66,38 -58,24 -73,19 -62,8 -76,0 -62,-8 -73,-19 -58,-24 -66,-38 -50,-38 -54,-54 -38,-50 -38,-66 -24,-58 -19,-73 -8,-62"/>
      <circle r="52" fill="var(--white)"/>
      <circle r="48" fill="var(--badge-grey)"/>
      <g transform="rotate(12)">
        <text class="badge__text" x="0" y="-4" text-anchor="middle">LIMITED</text>
        <text class="badge__text" x="0" y="26" text-anchor="middle">TIME.</text>
      </g>
    </svg>
  </section>

  <section class="card card--back">
    <header class="banner">
      <svg width="624" height="56" viewBox="0 0 624 56" aria-hidden="true">
        <polygon points="0,0 614,0 624,56 0,56" fill="var(--banner)"/>
        <polyline points="614,0 624,56 0,56" fill="none" stroke="var(--banner-edge)" stroke-width="2"/>
      </svg>
      <h2 class="banner__title">Bluebonnet Hearing Aid Device Center.</h2>
    </header>

    <div class="promo">
      <div class="promo__welcome">Walk-in Welcome</div>
      <div class="promo__sub">Appointments appreciated.</div>
      <div class="promo__headline">THIS MONTH ONLY</div>
      <div class="promo__detail">Special discounts on new state of<br>the art hearing aids w/remote.</div>
    </div>

    <div class="located">Located at</div>
    <address class="contact" style="font-style:normal">
      <div class="contact__line contact__line--big">417 Marwick Ln Abilene Texas 79488</div>
      <div class="contact__line contact__line--big">Ph 325-555-0147.</div>
      <div class="contact__line contact__line--small contact__line--gap">Hours Mon thru Thurs 9:00am - 5:00pm</div>
      <div class="contact__line contact__line--small">Closed for lunch 12:00pm - 1:00pm . Open 9:00am - 1:00pm</div>
    </address>
  </section>

</main>
</body>
</html>
```